General Surgeon flyer to be distributed to GPs

I am a general surgeon and I would like to have a flyer designed aiming to introduce myself to GPs.

Name: Dr Tobias Kellingford MD, FSCSP
Address: Suite 4C, Brayfield private hospital, 418 Copperleaf Parade, Hollowmere, VIC, 3187
T: (03) 9561 8027
F: (03) 9773 4105
E: referrals@yourtheatrewellnessportal.com.au
Website: www.yourtheatrewellnessportal.com.au

Tobias is a highly trained general surgeon, having completed extensive surgical training at Coastal Ridge health, Pellbrook and Tarrowby Health networks. He further specialized by completing a fellowship in Oesophagogastric and Bariatric Surgery at Greywater Infirmary Melbourne, one of Victoria’s leading Upper GI surgical centres.

With expertise in both advanced laparoscopic and open surgical techniques, he performs a wide range of procedures involving the gastrointestinal system, abdominal wall hernias, as well as other major and minor general surgical operations. In addition to holding appointments at Coastal Ridge Health, he also operates at Brayfield and Ashcombe Private Hospitals.

Dr Kellingford is committed to providing patient-centred care with a focus on surgical precision, safety, and long-term health outcomes.

He is also fluent in Farsi/Pesrian.
Outside of surgery, Tobias enjoys playings classical piano and spending time with his 6-year-old Bordoodle on long walks.

Upper GI & Bariatric Surgery:
Hiatus hernia repair, sleeve gastrectomy, gastric bypass
General Surgery conditions:
Gallbladder Surgery: Laparoscopic cholecystectomy
Hernia Repair: Laparoscopic and open surgery (inguinal,
umbilical, incisional)
Anorectal Procedures: Haemorrhoidectomy, haemorrhoid banding
Hand Surgery: Carpal tunnel release, Lymph Node Biopsy
Ingrown Toenail Surgery
Skin & Soft Tissue Surgery: Skin cancer removal, lipoma and
sebaceous cyst excision
Emergency Surgery: Laparotomy, Appendicectomy, bowel resection
Endoscopy: Diagnostic and therapeutic procedures

```html
<!DOCTYPE html>
<html lang="en">
<head>
<meta charset="utf-8">
<title>Dr Tobias Kellingford – GP Introduction Flyer</title>
<link href="https://fonts.googleapis.com/css2?family=Montserrat:wght@400;500;600;700;800;900&display=swap" rel="stylesheet">
<style>
  :root{
    --page:#efefef;
    --grey-top:#b7b8ba;
    --grey-map:#c9cacc;
    --phone-band:#6189b9;
    --pale-band:#dde9f7;
    --navy:#16457a;
    --navy-deep:#0d3360;
    --blue-body:#174a82;
    --title-blue:#7aa6dc;
    --list-bg:#dfeefc;
    --ink:#12335e;
    --ink-soft:#2a3f5c;
    --badge-band:#e5e6e8;
    --address-band:#d2d3d5;
    --brand:#1c78bf;
    --white:#ffffff;
  }
  *{box-sizing:border-box;margin:0;padding:0}
  html,body{width:1200px;height:729px;overflow:hidden}
  body{background:var(--page);font-family:"Montserrat",sans-serif;position:relative}
  .sheet{position:absolute;top:98px;width:376px;height:532px;overflow:hidden;background:var(--white)}
  .sheet--front{left:153px}
  .sheet--back{left:668px}

  /* front */
  .hero{position:absolute;left:0;top:0;width:376px;height:349px;background:var(--grey-top)}
  .hero__map{position:absolute;left:0;top:110px;width:376px;height:239px;background:linear-gradient(160deg,var(--grey-map),#bfc0c2)}
  .hero__portrait{position:absolute;left:50px;top:110px;width:272px;height:239px;background:linear-gradient(180deg,#b9a49a 0%,#8c8fa3 40%,#3c4c7a 60%,#2f3f6b 100%);border-radius:110px 110px 0 0;opacity:.9}
  .hero__name{position:absolute;left:31px;top:52px;color:var(--white);font-weight:900;font-size:21.5px;line-height:21px;letter-spacing:.2px}
  .hero__creds{display:block;font-weight:600;font-size:15px;line-height:20px;margin-top:1px}
  .brand{position:absolute;right:31px;top:96px;display:flex;align-items:center;gap:6px;color:var(--brand);font-size:8.5px;font-weight:500;letter-spacing:.8px;text-transform:uppercase;text-align:right;line-height:11px}
  .brand__dot{width:14px;height:14px;border-radius:50%;background:var(--brand);flex:none}

  .phone-band{position:absolute;left:0;top:349px;width:376px;height:49px;background:var(--phone-band);color:var(--white);text-align:center}
  .phone-band__number{display:flex;justify-content:center;align-items:center;gap:6px;margin-top:7px;font-weight:700;font-size:20.5px;letter-spacing:.3px;line-height:22px}
  .phone-band__web{font-size:8.8px;letter-spacing:1.9px;margin-top:3px}
  .contact-band{position:absolute;left:0;top:398px;width:376px;height:17px;background:var(--pale-band);display:flex;justify-content:space-between;align-items:center;padding:0 30px;color:var(--ink)}
  .contact-band__email{font-size:6.2px;letter-spacing:.8px}
  .contact-band__fax{display:flex;align-items:center;gap:3px;font-weight:700;font-size:9px}
  .intro{position:absolute;left:0;top:415px;width:376px;height:117px;background:var(--navy);color:var(--white)}
  .intro__text{margin:7px 30px 0 30px;font-size:7.6px;line-height:10.3px;text-align:justify}
  .intro__button{position:absolute;left:138px;top:73px;width:106px;height:21px;border:1px solid var(--white);border-radius:11px;display:flex;align-items:center;justify-content:center;gap:4px;font-size:7.4px}

  /* back */
  .back-web{position:absolute;left:0;top:0;width:376px;height:54px;text-align:center;padding-top:34px;font-size:8.6px;letter-spacing:1.9px;color:var(--ink)}
  .back-title{position:absolute;left:0;top:54px;width:376px;height:27px;background:var(--navy-deep);color:var(--title-blue);text-align:center;font-size:10.8px;line-height:27px;font-weight:800}
  .back-title span{font-weight:500;margin-left:4px}
  .bio{position:absolute;left:0;top:81px;width:376px;height:132px;background:var(--blue-body);color:var(--white);padding:12px 29px 0 30px;font-size:7.4px;line-height:10.2px}
  .bio p{text-align:justify;margin-bottom:8px}
  .bio p:nth-child(n+2){text-align:left}
  .services{position:absolute;left:0;top:213px;width:376px;height:207px;background:var(--list-bg);padding:14px 30px 0 40px;list-style:none;color:var(--ink-soft)}
  .services li{position:relative;font-size:7.3px;line-height:10px;margin-bottom:4.2px}
  .services li::before{content:"";position:absolute;left:-8px;top:3px;width:3.4px;height:3.4px;border-radius:50%;background:var(--ink)}
  .services strong{display:block;color:var(--ink);font-weight:700;font-size:7.4px;letter-spacing:.2px}
  .badges{position:absolute;left:0;top:420px;width:376px;height:48px;background:var(--badge-band);display:flex;align-items:center;justify-content:center;gap:26px}
  .badge{display:flex;align-items:center;gap:7px;color:var(--ink);font-size:7.4px;line-height:9.5px}
  .badge__square{width:16px;height:16px;background:var(--navy)}
  .badge__circle{width:35px;height:35px;border-radius:50%;background:linear-gradient(135deg,#2dbb6a,#25a7e0)}
  .address{position:absolute;left:0;top:468px;width:376px;height:15px;background:var(--address-band);text-align:center;font-size:5.6px;line-height:15px;color:var(--ink)}
  .back-foot{position:absolute;left:0;top:483px;width:376px;height:49px;display:flex;justify-content:space-between;align-items:center;padding:0 30px}
  .back-foot__links{font-size:4.6px;letter-spacing:.7px;line-height:6.2px;color:var(--ink)}
  .back-foot__phone{display:flex;align-items:center;gap:7px;font-weight:700;font-size:15px;color:var(--ink)}
</style>
</head>
<body>
  <section class="sheet sheet--front">
    <div class="hero">
      <div class="hero__map" role="img" aria-label="Faint map of Australia in light grey"></div>
      <div class="hero__portrait" role="img" aria-label="Portrait photograph of the surgeon in a navy suit"></div>
      <h1 class="hero__name">DR TOBIAS<br>KELLINGFORD<span class="hero__creds">MD, FSCSP</span></h1>
      <div class="brand"><span class="brand__dot"></span><span>Southbank<br>Surgical Group</span></div>
    </div>
    <div class="phone-band">
      <div class="phone-band__number">
        <svg width="12" height="19" viewBox="0 0 12 19"><rect x="1" y="1" width="10" height="17" rx="1.8" fill="none" stroke="#fff" stroke-width="1.3"/><line x1="4.5" y1="15.5" x2="7.5" y2="15.5" stroke="#fff" stroke-width="1"/></svg>
        (03) 9561 8027
      </div>
      <div class="phone-band__web">www.yourtheatrewellnessportal.com.au</div>
    </div>
    <div class="contact-band">
      <span class="contact-band__email">referrals@yourtheatrewellnessportal.com.au</span>
      <span class="contact-band__fax">
        <svg width="10" height="9" viewBox="0 0 10 9"><rect x="2.5" y=".5" width="5" height="3" fill="none" stroke="#12335e" stroke-width=".8"/><rect x=".5" y="3" width="9" height="4" rx=".8" fill="none" stroke="#12335e" stroke-width=".8"/><rect x="2.5" y="5.5" width="5" height="3" fill="#fff" stroke="#12335e" stroke-width=".8"/></svg>
        (03) 9773 4105
      </span>
    </div>
    <div class="intro">
      <p class="intro__text">Tobias is a highly trained general surgeon, having completed extensive surgical training at Coastal Ridge health, Pellbrook and Tarrowby Health networks. He further specialized by completing a fellowship in Oesophagogastric and Bariatric Surgery at Greywater Infirmary Melbourne, one of Victoria’s leading Upper GI surgical centres.</p>
      <div class="intro__button">
        <svg width="10" height="9" viewBox="0 0 10 9"><path d="M1 1 L4 4.5 L1 8 Z M9 1 L6 4.5 L9 8 Z" fill="none" stroke="#fff" stroke-width=".8"/><line x1="5" y1="0" x2="5" y2="9" stroke="#fff" stroke-width=".8"/></svg>
        See Back for More
      </div>
    </div>
  </section>

  <section class="sheet sheet--back">
    <div class="back-web">www.yourtheatrewellnessportal.com.au</div>
    <h2 class="back-title">DR TOBIAS KELLINGFORD<span>MD, FSCSP</span></h2>
    <div class="bio">
      <p>With expertise in both advanced laparoscopic and open surgical techniques, he performs a wide range of procedures involving the gastrointestinal system, abdominal wall hernias, as well as other major and minor general surgical operations. In addition to holding appointments at Coastal Ridge Health, he also operates at Brayfield and Ashcombe Private Hospitals.</p>
      <p>Dr Kellingford is committed to providing patient-centred care with a focus on surgical precision, safety, and long-term health outcomes.</p>
      <p>He is also fluent in Farsi/Pesrian. Outside of surgery, Tobias enjoys playings classical piano and spending time with his 6-year-old Bordoodle on long walks.</p>
    </div>
    <ul class="services">
      <li><strong>UPPER GI &amp; BARIATRIC SURGERY</strong>Upper GI &amp; Bariatric Surgery:</li>
      <li><strong>GENERAL SURGERY CONDITIONS</strong>Gallbladder Surgery: Laparoscopic cholecystectomy</li>
      <li><strong>HERNIA REPAIR</strong>Laparoscopic and open surgery (inguinal, umbilical, incisional)</li>
      <li><strong>ANORECTAL PROCEDURES</strong>Haemorrhoidectomy, haemorrhoid banding</li>
      <li><strong>HAND SURGERY</strong>Carpal tunnel release, Lymph Node Biopsy Ingrown Toenail Surgery</li>
      <li><strong>SKIN &amp; SOFT TISSUE SURGERY</strong>Skin cancer removal, lipoma and sebaceous cyst excision</li>
      <li><strong>EMERGENCY SURGERY</strong>Laparotomy, Appendicectomy, bowel resection Endoscopy: Diagnostic and therapeutic procedures</li>
    </ul>
    <div class="badges">
      <div class="badge"><span class="badge__square"></span><span>Fellow of the Southern College<br>of Surgical Practice</span></div>
      <span class="badge__circle"></span>
    </div>
    <div class="address">Suite 4C, Brayfield private hospital, 418 Copperleaf Parade, Hollowmere, VIC, 3187</div>
    <div class="back-foot">
      <div class="back-foot__links">www.yourtheatrewellnessportal.com.au<br>referrals@yourtheatrewellnessportal.com.au</div>
      <div class="back-foot__phone">
        <svg width="9" height="14" viewBox="0 0 9 14"><rect x=".7" y=".7" width="7.6" height="12.6" rx="1.4" fill="none" stroke="#12335e" stroke-width="1"/><line x1="3.5" y1="11.3" x2="5.5" y2="11.3" stroke="#12335e" stroke-width=".8"/></svg>
        (03) 9561 8027
      </div>
    </div>
  </section>
</body>
</html>
```